Web Design Project

Hi, we need a new and professional design for our company "partnertradingcircuit". The website should communicate business but with a friendly and professional touch.

You can use the following categories for the menu;

Home - customer groups - products - voucher system- contact

Give it your best,

Regards,
Anselm

Industry/Entity Type

Business

```html
<!DOCTYPE html>
<html lang="en">
<head>
<meta charset="utf-8">
<title>Partner Trading Circuit</title>
<link rel="stylesheet" href="https://fonts.googleapis.com/css2?family=Arimo:wght@400;700&display=swap">
<style>
:root{
  --navy:#0d2f55;
  --hero:#1d5d9c;
  --hero-dark:#0b3566;
  --accent:#f5a01a;
  --link:#1b5ea8;
  --title:#1f5f9e;
  --text:#555;
  --light:#f1f1f1;
  --line:#d9d9d9;
  --footer:#222;
  --footer-bottom:#111;
  --white:#fff;
}
*{box-sizing:border-box;margin:0;padding:0}
html,body{width:780px;height:1200px;overflow:hidden}
body{font-family:"Arimo",Arial,sans-serif;color:var(--text);background:var(--white);position:relative;font-size:8px;line-height:1.5}
.abs{position:absolute}
.site-header{left:0;top:0;width:780px;height:47px;background:linear-gradient(var(--navy),#123e6e);border-bottom:1px solid #2a5f97}
.brand{left:72px;top:13px;display:flex;align-items:center;gap:6px;color:var(--white);font-size:13px}
.brand-mark{width:14px;height:14px;border-radius:50%;background:var(--accent)}
.main-nav{right:60px;top:16px;display:flex;gap:26px;font-size:10px;color:var(--white)}
.main-nav .current{color:var(--accent)}
.hero{left:0;top:47px;width:780px;height:273px;background:radial-gradient(ellipse at 55% 40%,#3a82c6,var(--hero) 45%,var(--hero-dark))}
.hero h1{position:absolute;left:120px;top:26px;font-weight:400;font-size:24px;color:var(--white)}
.hero-text{position:absolute;left:120px;top:75px;width:275px;color:#dbe8f5;font-size:7.5px;line-height:1.75}
.hero-photo{position:absolute;left:397px;top:78px;width:260px;height:155px;border:4px solid #e9eef3;background:linear-gradient(135deg,#d9dde2,#8e969e);border-radius:2px}
.arrow{position:absolute;top:122px}
.read-more{position:absolute;left:293px;top:214px;width:88px;height:24px;border-radius:12px;background:linear-gradient(#ffc23a,#f08a00);color:var(--white);font-size:9px;font-weight:700;display:flex;align-items:center;justify-content:center;gap:5px}
.read-more i{width:11px;height:11px;border-radius:50%;background:#c26a00;display:block}
.thumb-strip{left:0;top:320px;width:780px;height:83px;background:linear-gradient(#e6e6e6,#f9f9f9 60%,#dcdcdc)}
.thumb{position:absolute;top:13px;width:53px;height:53px;background:var(--white);border:1px solid #ccc;padding:4px}
.thumb span{display:block;width:100%;height:100%;background:linear-gradient(135deg,#c8ccd1,#5c6670)}
.features{left:0;top:403px;width:780px;height:170px;background:linear-gradient(#dfe9f2,#fff 60%)}
.feature{position:absolute;top:0;width:200px;height:170px;border-left:1px solid #e3e7eb;padding:14px 12px 0 38px}
.feature h2{font-weight:400;font-size:16px;color:var(--title);margin-left:-8px;display:flex;align-items:center;gap:6px}
.feature h2 i{width:18px;height:18px;border-radius:50%;background:#2d78c4;display:block;margin-left:-20px}
.feature p{margin-top:4px;width:150px;font-size:7.5px}
.btn-grey{position:absolute;right:14px;top:152px;width:56px;height:14px;border-radius:7px;background:linear-gradient(#c5c5c5,#8d8d8d);color:var(--white);font-size:6.5px;display:flex;align-items:center;justify-content:center}
.welcome{left:72px;top:590px;width:442px}
.section-title{font-weight:400;font-size:19px;color:var(--title);padding-bottom:3px;border-bottom:1px solid var(--line);margin-bottom:6px}
.welcome p{font-size:7.5px;margin-bottom:11px}
.featured{left:72px;top:765px;width:442px}
.product{position:absolute;top:40px;width:129px;height:172px;border:1px solid var(--line);border-radius:4px;background:var(--white);box-shadow:0 1px 3px rgba(0,0,0,.12);text-align:center}
.product-img{position:absolute;left:38px;top:12px;width:54px;height:82px;background:linear-gradient(#7aa85a,#3c6e3a)}
.price-tag{position:absolute;left:-6px;top:6px;width:58px;height:18px;background:#e5461b;color:var(--white);font-size:7px;transform:rotate(-38deg);display:flex;align-items:center;justify-content:center}
.product p{position:absolute;left:3px;right:3px;top:112px;font-size:9.3px;color:#444;line-height:1.25}
.product-actions{position:absolute;left:7px;right:7px;top:146px;display:flex;justify-content:space-between}
.product-actions span{border:1px solid #ccc;border-radius:3px;font-size:6.5px;font-weight:700;color:var(--link);padding:3px 0;width:53px}
.side-box{position:absolute;left:533px;width:175px;border:1px solid var(--line);border-radius:3px;background:var(--white)}
.side-box h3{background:linear-gradient(#f2f2f2,#dedede);font-weight:400;font-size:11.5px;color:#333;padding:6px 9px}
.cat-list{list-style:none;padding:2px 9px}
.cat-list li{font-size:7.5px;color:var(--link);padding:4px 0 4px 12px;border-bottom:1px solid #eee;position:relative}
.cat-list li::before,.footer-col li::before{content:"»";position:absolute;left:0}
.view-all{text-align:right;font-size:7.5px;color:var(--link);padding:4px 9px 6px}
.news{padding:5px 9px 0}
.news h4{font-weight:400;font-size:9.5px;color:var(--link)}
.news-item{display:flex;gap:5px;margin:2px 0 6px}
.news-item span{width:32px;height:32px;flex:none;background:linear-gradient(#c8ccd1,#4a5460);border:1px solid #ddd}
.news-item p{font-size:7px;line-height:1.4}
.site-footer{left:0;top:1011px;width:780px;height:156px;background:var(--footer);color:#ddd}
.footer-col{position:absolute;top:13px}
.footer-col h5{font-weight:400;font-size:11.5px;color:var(--white);margin-bottom:5px}
.footer-col ul{list-style:none}
.footer-col li{position:relative;padding-left:8px;font-size:7.5px;line-height:2.05}
.contacts p{font-size:9px;line-height:1.6}
.field{width:124px;height:18px;background:var(--white);border-radius:2px;margin-bottom:6px;font-size:7px;color:#aaa;padding:4px 5px}
.subscribe{margin-left:50px;width:74px;height:21px;border-radius:3px;background:linear-gradient(#ffc23a,#f08a00);color:#222;font-size:8.5px;display:flex;align-items:center;justify-content:center}
.footer-bottom{left:0;top:1167px;width:780px;height:33px;background:var(--footer-bottom);color:#ddd;font-size:8px}
.footer-bottom .copy{position:absolute;left:72px;top:11px}
.follow{position:absolute;right:60px;top:8px;display:flex;align-items:center;gap:5px;font-size:11px}
.follow span{width:15px;height:15px;border-radius:3px;background:#4a78b5;display:block}
</style>
</head>
<body>
<header class="site-header abs">
  <div class="brand abs"><span class="brand-mark"></span>Partner Trading Circuit</div>
  <nav class="main-nav abs"><span class="current">Home</span><span>Customer groups »</span><span>Products</span><span>Voucher System</span><span>Contact Us</span></nav>
</header>

<section class="hero abs">
  <h1>Lorem ipsum dolor sit amet consectetur</h1>
  <p class="hero-text">Proin sed diam et nisl commodo pharetra. Cras non sapien vehicula neque feugiat tempus eu mollis metus. Phasellus dui elit, blandit euismod commodo eget, ultricies consequat erat. Proin mollis pulvinar pulvinar. Nunc sem massa, dictum sed dictum eu, iaculis vestibulum libero. In hac habitasse platea dictumst. Pellentesque mattis tincidunt interdum. Phasellus eget nisi arcu, sit amet malesuada lorem. Nulla semper consequat ante, et rutrum libero convallis et. Duis accumsan libero et lectus vulputate vehicula. Sed ultricies, ante sit amet scelerisque rutrum, libero erat vestibulum sapien, porta auctor ante orci quis augue.</p>
  <div class="hero-photo" role="img" aria-label="Photo of a business team meeting around a table"></div>
  <svg class="arrow" style="left:71px" width="36" height="30" viewBox="0 0 36 30"><path d="M0 15 17 0v8h19v14H17v8z" fill="#3f8fd6"/></svg>
  <svg class="arrow" style="left:673px" width="36" height="30" viewBox="0 0 36 30"><path d="M36 15 19 0v8H0v14h19v8z" fill="#3f8fd6"/></svg>
  <div class="read-more"><i></i>read more</div>
  <svg class="abs" style="left:143px;top:265px" width="16" height="8" viewBox="0 0 16 8"><path d="M0 0h16L8 8z" fill="#0b3566"/></svg>
</section>

<section class="thumb-strip abs">
  <div class="thumb" style="left:125px"><span role="img" aria-label="Business team thumbnail"></span></div>
  <div class="thumb" style="left:203px"><span role="img" aria-label="Meeting thumbnail"></span></div>
  <div class="thumb" style="left:284px"><span role="img" aria-label="Office team thumbnail"></span></div>
  <div class="thumb" style="left:363px"><span role="img" aria-label="Group thumbnail"></span></div>
  <div class="thumb" style="left:443px"><span role="img" aria-label="Colleagues thumbnail"></span></div>
  <div class="thumb" style="left:520px"><span role="img" aria-label="Presentation thumbnail"></span></div>
  <div class="thumb" style="left:600px"><span role="img" aria-label="Partners thumbnail"></span></div>
</section>

<section class="features abs">
  <div class="feature" style="left:89px"><h2><i></i>About Us</h2><p>Lorem ipsum dolor sit amet, consectetur adipiscing elit. Donec dignissim eleifend fermentum. Ut facilisis elit non lorem laoreet ac suscipit enim tempus. Integer ullamcorper pulvinar arcu. Nullam in porta arcu. Pellentesque lacinia tempus sem id facilisis.</p><span class="btn-grey">Read More</span></div>
  <div class="feature" style="left:289px"><h2><i></i>Testimonials</h2><p>Lorem ipsum dolor sit amet, consectetur adipiscing elit. Donec dignissim eleifend fermentum. Ut facilisis elit non lorem laoreet ac suscipit enim tempus. Integer ullamcorper pulvinar arcu. Nullam in porta arcu. Pellentesque lacinia tempus sem id facilisis.</p><span class="btn-grey">Read More</span></div>
  <div class="feature" style="left:489px;border-right:1px solid #e3e7eb"><h2><i></i>Services</h2><p>Lorem ipsum dolor sit amet, consectetur adipiscing elit. Donec dignissim eleifend fermentum. Ut facilisis elit non lorem laoreet ac suscipit enim tempus. Integer ullamcorper pulvinar arcu. Nullam in porta arcu. Pellentesque lacinia tempus sem id facilisis.</p><span class="btn-grey">Read More</span></div>
</section>

<section class="welcome abs">
  <h2 class="section-title">Welcome to our website</h2>
  <p>Lorem ipsum dolor sit amet, consectetur adipiscing elit. Suspendisse et odio et nulla dignissim eleifend. Donec blandit est nec dui pellentesque vestibulum. Vivamus tincidunt dui a sem ornare luctus. Aliquam tristique dui a tortor consequat fringilla. Quisque eleifend fringilla risus, non accumsan nisi faucibus vitae. Quisque sit amet enim ac risus sollicitudin dictum. Nullam at pretium enim.</p>
  <p>Duis consectetur justo accumsan eros consequat feugiat. Aliquam adipiscing, erat ut hendrerit gravida, est turpis eleifend elit, a iaculis purus lorem quis nisl. Etiam dapibus elit eget sem vulputate et auctor quam feugiat. Pellentesque vehicula tempus vestibulum. Cras dui tortor, interdum vel dignissim non, rutrum ut odio. Suspendisse vitae lobortis ligula. Cras odio dolor, rutrum at pretium ut, pulvinar at dui. In pharetra fermentum sem vestibulum venenatis. Sed fringilla accumsan justo in rhoncus. Aliquam sodales nulla et mauris hendrerit cursus. Integer feugiat nulla sit amet sapien ultricies vulputate pharetra enim tristique. Phasellus ut sollicitudin eros.</p>
</section>

<section class="featured abs">
  <h2 class="section-title">Featured Products</h2>
  <div class="product" style="left:12px"><div class="product-img" role="img" aria-label="Green product package"></div><span class="price-tag">Price: $44.20</span><p>Lorem ipsum dolor sit amet<br>consectetur adipiscing elit.</p><div class="product-actions"><span>DETAILS</span><span>ADD TO CARD</span></div></div>
  <div class="product" style="left:161px"><div class="product-img" style="left:30px;top:22px;width:70px;height:68px;background:linear-gradient(#e8d6a6,#b88a44)" role="img" aria-label="Tan product box"></div><span class="price-tag">Price: $44.20</span><p>Lorem ipsum dolor sit amet<br>consectetur adipiscing elit.</p><div class="product-actions"><span>DETAILS</span><span>ADD TO CARD</span></div></div>
  <div class="product" style="left:311px"><div class="product-img" role="img" aria-label="Green product package"></div><span class="price-tag">Price: $44.20</span><p>Lorem ipsum dolor sit amet<br>consectetur adipiscing elit.</p><div class="product-actions"><span>DETAILS</span><span>ADD TO CARD</span></div></div>
</section>

<aside class="side-box" style="top:597px">
  <h3>Browse By Categories</h3>
  <ul class="cat-list">
    <li>Lorem ipsum dolor sit amet</li><li>Consectetur adipiscing</li><li>Suspendisse et odio et nulla</li><li>Quisque eleifend fringilla risus</li><li>Lorem ipsum dolor sit amet</li><li>Consectetur adipiscing</li><li>Suspendisse et odio et nulla</li>
  </ul>
  <div class="view-all">View All</div>
</aside>

<aside class="side-box" style="top:805px">
  <h3>Latest News</h3>
  <div class="news">
    <h4>Lorem ipsum dolor sit amet</h4>
    <div class="news-item"><span role="img" aria-label="Portrait of a businessman"></span><p>Lorem ipsum dolor sit amet, consectetur adipiscing elit. Suspendisse et odio et nulla dignissim eleifend. Donec blandit est</p></div>
    <h4>Lorem ipsum dolor sit amet</h4>
    <div class="news-item"><span role="img" aria-label="Portrait of a businessman"></span><p>Lorem ipsum dolor sit amet, consectetur adipiscing elit. Suspendisse et odio et nulla dignissim eleifend. Donec blandit est</p></div>
  </div>
  <div class="view-all">View All</div>
</aside>

<footer class="site-footer abs">
  <div class="footer-col" style="left:72px"><h5>Information</h5><ul><li>Home</li><li>Customer Service</li><li>Privacy Policy</li><li>Site Map</li><li>Orders and Returns</li><li>Contact Us</li></ul></div>
  <div class="footer-col" style="left:197px"><h5>Why buy from us</h5><ul><li>Shipping &amp; Returns</li><li>Secure Shopping</li><li>International Shipping</li><li>Affiliates</li><li>Group Sales</li></ul></div>
  <div class="footer-col" style="left:322px"><h5>My account</h5><ul><li>Sign In</li><li>View Cart</li><li>My Wishlist</li><li>Track My Order</li><li>Help</li></ul></div>
  <div class="footer-col contacts" style="left:441px"><h5>Contacts Us</h5><p>Lorem ipsum dolor sit amet<br>consectetur adipiscing elit<br>Telephone: 1234567890<br>Fax: 1234567890<br>Email: info@partnertrading.example</p></div>
  <div class="footer-col" style="left:582px"><h5>Newsletter Signup</h5><div class="field">Your Full Name</div><div class="field">Your Email Address</div><div class="subscribe">Subscribe</div></div>
</footer>

<div class="footer-bottom abs">
  <span class="copy">© 2013 Partner Trading Circuit. All Rights Reserved.</span>
  <div class="follow">Follow us on: <span></span><span></span><span></span><span></span></div>
</div>
</body>
</html>
```